Bramblewood Craft Spirits Bottle Label

Bramblewood Craft Spirits is a distillery and craft cocktail bar that will be located in Calgary, Alberta, Canada. Here, we create awesome hand crafted spirits like vodka, gin, rum, whiskey, brandy, liqueurs etc. We need bottle labels for 3 different initial products. The names of the products are as follows, Orchard Dash Gin (22% alc/vol), Toverin Dry Gin (40% alc/vol), and Palundro Contemporary Gin (40% alc/vol). It would be preferable to have 3 distinct labels. The alcohol by volume declaration must be on the front display of the label, without having to turn the bottle. There is a logo for Bramblewood Craft Spirits I would like featured in the front around 1''x1" or 2.5cm x 2.5cm in size. Some last minute changes are being made to the logo so it is not uploaded at this moment. Abstract geometry would be a great fit for the contemporary gin and I have attached an example.Simple or complex designs both encouraged. The Orchard Dash Gin will be in the Moonea style bottle and the other two will be in Apotheker style bottles. Thank you so much to anyone interested in participating and we can't wait to hear from you. This is a great opportunity to showcase your creativity and be involved with future products!
Young professionals ages 21-30.

```html
<!DOCTYPE html>
<html lang="en">
<head>
<meta charset="utf-8">
<title>Orchard Dash Gin – Bottle Label</title>
<link rel="stylesheet" href="https://fonts.googleapis.com/css2?family=Cinzel:wght@400;600;700&family=Cinzel+Decorative:wght@700;900&display=swap">
<style>
  :root {
    --page: #ffffff;
    --label: #ffffff;
    --gold: #b8894a;
    --gold-light: #e6c27a;
    --gold-dark: #8a5f2b;
    --ink: #2f2f31;
    --leaf-grey: #d4d4d4;
    --lime: #9cc93c;
    --edge: #e2e2e2;
  }
  * { box-sizing: border-box; margin: 0; padding: 0; }
  html, body {
    width: 1102px; height: 1200px; overflow: hidden;
    background: var(--page);
  }
  .canvas { position: relative; width: 1102px; height: 1200px; }

  .label {
    position: absolute; left: 33px; top: 84px;
    width: 1035px; height: 1032px;
    background: var(--label);
    border: 1px solid var(--edge);
    overflow: hidden;
  }

  .art { position: absolute; }
  .art--leaves-top {
    left: 720px; top: 0; width: 315px; height: 495px;
    background: radial-gradient(ellipse at 60% 45%, #cfcfcf 0%, #e4e4e4 55%, rgba(255,255,255,0) 78%);
  }
  .art--leaves-bottom {
    left: 0; top: 705px; width: 600px; height: 327px;
    background: radial-gradient(ellipse at 45% 75%, #cdcdcd 0%, #e6e6e6 50%, rgba(255,255,255,0) 76%);
  }
  .art--fruit-left {
    left: 0; top: 150px; width: 300px; height: 420px;
    background:
      radial-gradient(circle at 28% 52%, var(--lime) 0%, #c5e07d 22%, rgba(255,255,255,0) 36%),
      radial-gradient(ellipse at 62% 50%, #e7c89a 0%, #f3e2c6 42%, rgba(255,255,255,0) 70%);
  }
  .art--fruit-right {
    left: 585px; top: 615px; width: 420px; height: 417px;
    background:
      radial-gradient(circle at 78% 72%, var(--lime) 0%, #c5e07d 18%, rgba(255,255,255,0) 30%),
      radial-gradient(ellipse at 45% 62%, #e3bd87 0%, #f1dcbc 42%, rgba(255,255,255,0) 70%);
  }

  .frame {
    position: absolute; left: 285px; top: 237px;
    width: 460px; height: 606px;
    background: var(--label);
    border: 2px solid var(--gold);
  }

  .flourish {
    position: absolute; height: 14px;
    background: linear-gradient(90deg, rgba(184,137,74,0), var(--gold) 30%, var(--gold) 70%, rgba(184,137,74,0));
    border-radius: 7px; opacity: .8;
  }
  .flourish--top-left { left: 285px; top: 240px; width: 105px; height: 10px; top: 245px; }
  .flourish--top-right { left: 645px; top: 245px; width: 105px; height: 10px; }
  .flourish--title { left: 435px; top: 318px; width: 165px; }
  .flourish--bottom { left: 435px; top: 868px; width: 165px; }

  .brand-badge {
    position: absolute; left: 393px; top: 65px;
    width: 252px; height: 178px;
    background: linear-gradient(135deg, #c79a5c 0%, var(--gold) 45%, var(--gold-dark) 100%);
    display: flex; flex-direction: column; align-items: center; justify-content: center;
    font-family: "Cinzel", serif; font-weight: 600;
    color: #fbefd6; text-align: center;
  }
  .brand-badge__name { font-size: 20px; line-height: 1.35; letter-spacing: .5px; }
  .brand-badge__name span { display: block; font-size: 16px; letter-spacing: 6px; }

  .product-name {
    position: absolute; left: 285px; top: 345px; width: 460px;
    text-align: center; font-family: "Cinzel Decorative", serif; font-weight: 900;
  }
  .product-name__gold {
    display: block;
    background: linear-gradient(180deg, var(--gold-light) 0%, var(--gold) 50%, var(--gold-dark) 100%);
    -webkit-background-clip: text; background-clip: text; color: transparent;
  }
  .product-name__primary { font-size: 70px; line-height: 100px; }
  .product-name__secondary {
    display: block; font-family: "Cinzel", serif; font-weight: 700;
    font-size: 54px; line-height: 62px; color: var(--ink);
  }
  .product-name__type { font-size: 100px; line-height: 118px; }

  .tagline {
    position: absolute; left: 285px; top: 683px; width: 460px;
    text-align: center; font-family: "Cinzel", serif; font-weight: 400;
    font-size: 21px; line-height: 30px; color: #222;
  }

  .abv {
    position: absolute; left: 435px; top: 926px;
    width: 165px; height: 32px; border-radius: 16px;
    background: linear-gradient(90deg, var(--gold-dark), var(--gold), var(--gold-dark));
    color: #fbefd6; font-family: "Cinzel", serif; font-size: 17px;
    display: flex; align-items: center; justify-content: center; letter-spacing: .5px;
  }
</style>
</head>
<body>
<main class="canvas">
  <section class="label" aria-label="Orchard Dash Gin front label">
    <div class="art art--leaves-top" role="img" aria-label="Grey engraved citrus leaves and fruit"></div>
    <div class="art art--leaves-bottom" role="img" aria-label="Grey engraved citrus leaves and fruit"></div>
    <div class="art art--fruit-left" role="img" aria-label="Gold stippled orange with a green lime slice and leaves"></div>
    <div class="art art--fruit-right" role="img" aria-label="Gold stippled oranges with a green lime slice and leaves"></div>

    <div class="flourish flourish--top-left" role="img" aria-label="Gold scroll ornament"></div>
    <div class="flourish flourish--top-right" role="img" aria-label="Gold scroll ornament"></div>

    <div class="frame"></div>

    <div class="brand-badge">
      <p class="brand-badge__name">BRAMBLEWOOD CRAFT<span>SPIRITS</span></p>
    </div>

    <div class="flourish flourish--title" role="img" aria-label="Gold scroll ornament"></div>

    <h1 class="product-name">
      <span class="product-name__gold product-name__primary">ORCHARD</span>
      <span class="product-name__secondary">DASH</span>
      <span class="product-name__gold product-name__type">GIN</span>
    </h1>

    <p class="tagline">Cool, elegant, refreshing<br>a brilliant combination<br>of gin &amp; Citrus Fruits</p>

    <div class="flourish flourish--bottom" role="img" aria-label="Gold scroll ornament"></div>

    <p class="abv">22% ALC/VOL</p>
  </section>
</main>
</body>
</html>
```